PIPE RELINING COMPANY NEEDS A NEW INFORMATIVE FLYER CREATED

We are a company that sells a service to residential homeowners (using a particular state of the art international product) and we need to refresh our A4 tri- fold flyer (z fold 6 pages). The layout needs to include pictures, heading and text boxes, but be simple and clean cut at the same time.

The front of the flyer must have the attached picture of the pipe under the house, logo and website.

This flyer is going to be given to clients and to leave with them when we quote for work.

Our colour scheme is black, white, red. A highlight colour if needed (in small amounts) could be 100% cyan and also a bright orange.

I have attached the copy of the text and this can be spread out throughout the brochure.

We are a professional and industry leading company so it needs to be professional, clean cut but with a modern edge.

Target Market(s)

HOMEOWNERS

Industry/Entity Type

It Company

Font styles to use
Sans Serif

Colors
ec1f27
ffffff
000000
f37122

Requirements
Must have
• PROFESSINAL, MODERN
• USE OF BLACK, RED AND WHITE - REFER LOGO
Should not have
• BE CLUTTERED

```html
<!DOCTYPE html>
<html lang="en">
<head>
<meta charset="utf-8">
<title>Clearline Pipe Relining – Tri-fold Flyer</title>
<link rel="stylesheet" href="https://fonts.googleapis.com/css2?family=Open+Sans:wght@400;700&display=swap">
<style>
  :root {
    --ink: #000000;
    --panel: #19191b;
    --paper: #ffffff;
    --red: #ec1f27;
    --grass: #5f8a3c;
    --soil: #7a4a2c;
    --sky: #9cc6e2;
  }
  * { box-sizing: border-box; margin: 0; padding: 0; }
  html, body { width: 1200px; height: 950px; overflow: hidden; background: var(--paper); }
  body { position: relative; font-family: "Open Sans", Arial, sans-serif; color: var(--ink); }

  .brand-box {
    position: absolute; background: var(--panel); color: var(--paper);
    display: flex; align-items: center; justify-content: center; gap: 12px;
  }
  .brand-mark { width: 18px; height: 18px; background: var(--red); }
  .brand-name { font-weight: 700; font-size: 34px; letter-spacing: 0.5px; color: var(--paper); }

  .photo { position: absolute; }
  .photo-roots {
    background: linear-gradient(180deg, var(--grass) 0%, #4d6d33 35%, var(--soil) 60%, #8a7a6a 100%);
  }
  .photo-home {
    background: linear-gradient(180deg, var(--sky) 0%, #c9c1a3 35%, var(--grass) 55%, var(--soil) 78%, #8a7a6a 100%);
  }

  /* Left panel */
  .about-title {
    position: absolute; left: 60px; top: 78px; width: 344px;
    text-align: center; font-weight: 700; font-size: 23px; line-height: 29px;
  }
  .about-list { position: absolute; left: 78px; top: 284px; width: 310px; font-size: 11.6px; line-height: 15.2px; }
  .about-list p { margin-bottom: 15.2px; }

  /* Middle panel */
  .why-title { position: absolute; left: 456px; top: 80px; font-weight: 700; font-size: 23px; }
  .why-list { position: absolute; left: 456px; top: 120px; width: 282px; font-size: 11.6px; line-height: 15.2px; }
  .why-list h3 { font-size: 11.6px; font-weight: 700; text-transform: uppercase; margin-bottom: 15.2px; }
  .why-list p { margin-bottom: 15.2px; }

  .contact-card { position: absolute; left: 431px; top: 645px; width: 312px; height: 261px; background: var(--panel); }
  .contact-card .brand-name { position: absolute; left: 20px; top: 18px; font-size: 34px; }
  .contact-card .brand-tag { position: absolute; right: 20px; top: 62px; color: var(--red); font-weight: 700; font-size: 18px; }
  .contact-lines {
    position: absolute; left: 50px; top: 93px; color: var(--paper);
    font-weight: 700; font-size: 14.5px; line-height: 20px; list-style: none;
  }

  /* Right panel (front) */
  .front { position: absolute; left: 792px; top: 66px; width: 358px; height: 859px; background: var(--panel); }
  .front-brand { position: absolute; left: 0; top: 0; width: 358px; height: 173px; flex-direction: column; gap: 4px; background: transparent; }
  .front-brand .brand-name { font-size: 40px; }
  .front-brand .brand-tag { color: var(--red); font-weight: 700; font-size: 19px; align-self: flex-end; margin-right: 38px; }
  .front-copy { position: absolute; left: 30px; top: 504px; width: 300px; color: var(--paper); font-size: 13.6px; line-height: 18.4px; }
  .front-copy p { margin-bottom: 18.4px; }
  .front-copy p.tight { margin-bottom: 0; }
</style>
</head>
<body>

  <!-- Left inner panel -->
  <h2 class="about-title">Things You Should Know<br>ABOUT</h2>
  <div class="brand-box" style="left:76px; top:149px; width:312px; height:90px;">
    <span class="brand-mark"></span><span class="brand-name">CLEARLINE</span>
  </div>
  <div class="about-list">
    <p>Knowledge &amp; Experience<br>We train other plumbers and have been doing it for over 10 years.</p>
    <p>We’re An Owned &amp; Operated Business<br>We take great pride in our work. Our business is based on relationships not transactions.</p>
    <p>We Use the best in class pipe relining solution<br>We have sourced the best products and equipment from around the world and our FlexLine product is from Germany.</p>
    <p>We have state of the art equipment.<br>Our truck is customer designed and filly equipped with latest technology to carry out pipe relining.</p>
    <p>We’re Fully licensed &amp; Insured<br>All of our technicians are fully licensed and qualified to complete the job. Our company is fully insured and are happy to provide you with documentation.</p>
    <p>After Sales Service<br>We don’t forget about you after the job and as part of the warranty we carry out an annual camera inspection of the drainage.</p>
  </div>
  <div class="photo photo-roots" role="img" aria-label="Cutaway illustration of tree roots wrapped around a relined underground pipe" style="left:53px; top:720px; width:357px; height:186px;"></div>

  <!-- Middle inner panel -->
  <h2 class="why-title">Why It Works:</h2>
  <div class="why-list">
    <h3>Clearline uses epoxy rein not polyester or silicate resins.</h3>
    <p>Why? Because epoxy resin does not shrink. Polyester and silicate resins can shrink in the pipe allowing tree roots to return.</p>
    <h3>Clearline inverts th eliner instead of using a drag-in method.</h3>
    <p>Why? Because this means that the resin has contact with the host pipe impregnating the cracks and joins the pipework. With the drag in method, the resin does not have contact with the host pipe and cannot impregnate the cracks and joins.</p>
    <h3>Clearline uses a German system called Veltaliner.</h3>
    <p>Why? Because it has been extensively tested in Europe and came out as the test winner in standard and extreme conditions based on all assessment criteria – effectiveness, density and load carrying capacity. Veltaliner has a proven track record and bee used to reline hundreds of kms throughout Europe.</p>
    <h3>Clearline provides a 25 year warranty</h3>
    <p>Why? Because we understand the quality of the equipment and product and how we install it. We were one of the first to reline in NSW and are constantly carrying out research and development.</p>
  </div>
  <div class="contact-card">
    <span class="brand-name" style="color:var(--paper);">CLEARLINE</span>
    <span class="brand-tag">Pipe Relining</span>
    <ul class="contact-lines">
      <li>42 HARBOUR RD.</li>
      <li>MILLBROOK, AS. 67120</li>
      <li>555-014-2278</li>
      <li>HELLO@CLEARLINERELINE.NET</li>
      <li>WWW.CLEARLINERELINE.COM</li>
    </ul>
  </div>

  <!-- Front panel -->
  <section class="front">
    <div class="brand-box front-brand">
      <span class="brand-name">CLEARLINE</span>
      <span class="brand-tag">Pipe Relining</span>
    </div>
    <div class="photo photo-home" role="img" aria-label="House with front lawn and a tree whose roots grip a relined drain pipe below ground" style="left:-2px; top:173px; width:360px; height:302px;"></div>
    <div class="front-copy">
      <p>Sewers back up in properties due to ageing lines, misaligned joints, root infestation, calcification and ground movement, costing property owners thousands of dollars in damage to their homes and landscaping.</p>
      <p class="tight">Pipe relining eliminates the need for costly excavations to expose and replace this damaged pipework.</p>
      <p>Pipe Relining is the process of installing a new pipe within the old.</p>
      <p>Why replace all of your drainage pipes when you can permanently repair the broken sections without destroying your environment.</p>
    </div>
  </section>

</body>
</html>
```